The Quiet Compass
Zielgruppe
Das Bundesforum Seelenheilkundiger Praxen e. V. (BFSP) ist ein Interessenverband mit 1.400 Mitgliedern, der sich für die Belange von psychotherapeutisch tätigen Psychologen, Ärzten und Kinder- und Jugendlichen-Psychotherapeuten einsetzt. Das Bundesforum Seelenheilkundiger Praxen wurde als Berufsverband am 2. Mai 2019 in Bonn gegründet.
Aufgabenstellung
Titel: The Quiet Compass - Das Arbeitsbuch der selten genutzten und vergessenen therapeutischen Werkzeuge im Behandlungsalltag
Kategorie: Sachbuch
Zielgruppe: nur Psychotherapeuten
Covergestaltung: Cover soll neugierig machen, aber nicht marktschreierisch sein, AIDA-Regel berücksichtigen,
„Augenfänger“, dezente Farben, nicht zu grell
Buchformat: 22x15.5 cm, ca. 530 Normseiten
Buchrücken: Titel und Autor
Ausführung: Hardcover, Softcover, Ebook
Autor: Rainer Holtkamp, Dipl.-Psychologe, ist Psychoanalytiker der Westfälischen Tiefenseelischen Gesellschaft, Kinder- und Jugendlichenpsychotherapeut, Psychologischer Psychotherapeut, Gruppenanalytiker, Lehrtherapeut und Supervisor. Neben seiner psychoanalytischen Ausbildung hat er noch Aus- und Weiterbildungen in Gruppentherapie, Gruppendynamik, Familientherapie, katathym imaginativer Psychotherapie und intensiver psychodynamischer Kurztherapie nach Davanloo. Seit 29 Jahren arbeitet er in seiner eigenen Praxis in Bonn. Neben seiner Praxistätigkeit arbeitet er als Gutachter im Antragsverfahren der gesetzlichen Krankenkassen und der Beihilfestellen. Er ist Gründer und 1. Vorsitzender des Bundesforums Seelenheilkundiger Praxen (BFSP) in Bonn.
Klappentext: „Wer liebt, was er tut, wird nie wieder arbeiten müssen.“ Ein kluger Aphorismus, der Konfuzius zugeschrieben wird. Psychotherapeuten lieben ihren Beruf. Dennoch ist die Arbeit mit kranken Menschen immer schwer und unberechenbar. Viele Erfahrungen und Erkenntnisse musste sich Rainer Holtkamp im Laufe seiner Berufstätigkeit von fast 30 Jahren selbst erarbeiten. In seiner Tätigkeit als Dozent und Supervisor konnte er viele Fragen der Kandidaten sammeln und daraus Interventionen erarbeiten. Interventionen, die meist in keinem Lehrbuch stehen. Mit vielen dieser Interventionen wird die psychotherapeutische Arbeit leichter und macht auch mehr Freude. Und wer mit Freude als Psychotherapeut in die Praxis geht, 'arbeitet' im Sinne ..

```html
<!DOCTYPE html>
<html lang="de">
<head>
<meta charset="utf-8">
<title>The Quiet Compass – Buchumschlag</title>
<link rel="stylesheet" href="https://fonts.googleapis.com/css2?family=Cabin+Sketch:wght@400;700&family=Patrick+Hand&family=Josefin+Sans:wght@400&family=Open+Sans:wght@400;700&display=swap">
<style>
  :root {
    --bg: #e6e6e4;
    --teal: #14a6aa;
    --teal-light: #2cc9cc;
    --teal-dark: #0e9195;
    --ink: #1c1c1c;
    --white: #ffffff;
    --sand: #c9955e;
    --sun: #f0dc63;
  }
  * { box-sizing: border-box; margin: 0; padding: 0; }
  html, body { width: 1200px; height: 800px; overflow: hidden; }
  body {
    background: var(--bg);
    position: relative;
    font-family: "Open Sans", sans-serif;
  }

  /* Spine */
  .spine {
    position: absolute;
    left: 70px; top: 60px;
    width: 56px; height: 680px;
    background: var(--white);
    display: flex; align-items: center; justify-content: center;
  }
  .spine-text {
    transform: rotate(-90deg);
    white-space: nowrap;
    font-family: "Josefin Sans", sans-serif;
    font-size: 20px;
    letter-spacing: 0.22em;
    color: var(--teal);
  }
  .spine-text .divider { color: var(--ink); margin: 0 0.6em; }
  .spine-text .spine-title { color: var(--ink); }

  /* Front cover */
  .front {
    position: absolute;
    left: 126px; top: 60px;
    width: 480px; height: 680px;
    background: linear-gradient(200deg, var(--teal-light) 0%, var(--teal) 35%, var(--teal-dark) 100%);
    color: var(--white);
    text-align: center;
  }
  .front-title { position: absolute; top: 56px; left: 0; right: 0; font-weight: normal; }
  .title-the {
    display: block;
    font-family: "Cabin Sketch", sans-serif;
    font-size: 44px; line-height: 1;
  }
  .title-main {
    display: block;
    font-family: "Cabin Sketch", sans-serif;
    font-weight: 700;
    font-size: 52px; line-height: 1.1;
    transform: rotate(-4deg);
    margin-top: 6px;
  }
  .front-subtitle {
    position: absolute; top: 210px; left: 40px; right: 40px;
    font-family: "Patrick Hand", cursive;
    font-size: 19px; line-height: 1.3;
    text-transform: uppercase;
  }
  .front-illustration {
    position: absolute; top: 320px; left: 100px;
    width: 280px; height: 200px;
    border-radius: 140px 140px 12px 12px;
    background: radial-gradient(circle at 50% 40%, var(--sun) 0%, #9fd6cf 45%, var(--sand) 80%);
    opacity: 0.9;
  }
  .front-author {
    position: absolute; top: 570px; left: 0; right: 0;
    font-family: "Josefin Sans", sans-serif;
    font-size: 24px; letter-spacing: 0.18em;
  }
  .audience-badge {
    position: absolute; top: 622px; left: 134px;
    width: 212px;
    border: 2px solid var(--ink);
    color: var(--ink);
    font-size: 17px;
    padding: 2px 6px;
    transform: rotate(-2deg);
  }

  /* Back cover */
  .back {
    position: absolute;
    left: 660px; top: 60px;
    width: 480px; height: 680px;
    background: var(--white);
    color: var(--teal);
    text-align: center;
    display: flex; flex-direction: column; align-items: center;
    padding: 40px 44px 34px;
  }
  .back-title { font-weight: normal; }
  .back-title .title-the { font-size: 30px; }
  .back-title .title-main { font-size: 38px; }
  .back-illustration {
    margin-top: 22px;
    width: 220px; height: 128px;
    border-radius: 110px 110px 10px 10px;
    background: linear-gradient(180deg, #d8f1f1 0%, #bfe7e8 100%);
    flex-shrink: 0;
  }
  .blurb {
    margin-top: 30px;
    width: 100%;
    color: var(--ink);
    text-align: justify;
    font-size: 10px; line-height: 1.32;
  }
  .blurb p + p { margin-top: 9px; }
  .back-audience {
    margin-top: auto;
    padding-top: 12px;
    font-weight: 700; font-size: 13px;
    color: var(--teal);
  }
</style>
</head>
<body>
  <div class="spine">
    <div class="spine-text">AUTOR NAME<span class="divider">|</span><span class="spine-title">THE QUIET COMPASS</span></div>
  </div>

  <section class="front">
    <h1 class="front-title">
      <span class="title-the">THE</span>
      <span class="title-main">QUIET COMPASS</span>
    </h1>
    <p class="front-subtitle">Das Arbeitsbuch<br>der selten genutzten<br>und vergessenen therapeutischen Werkzeuge<br>im Behandlungsalltag</p>
    <div class="front-illustration" role="img" aria-label="Illustration: Person liegt entspannt auf einer Therapiecouch vor einer aufgehenden Sonne"></div>
    <p class="front-author">AUTOR NAME</p>
    <p class="audience-badge">nur Psychotherapeuten</p>
  </section>

  <section class="back">
    <h2 class="back-title">
      <span class="title-the">THE</span>
      <span class="title-main">QUIET COMPASS</span>
    </h2>
    <div class="back-illustration" role="img" aria-label="Linienzeichnung: Person auf einer Therapiecouch vor aufgehender Sonne"></div>
    <div class="blurb">
      <p>„Wer liebt, was er tut, wird nie wieder arbeiten müssen.“ Ein kluger Aphorismus, der Konfuzius zugeschrieben wird.</p>
      <p>Psychotherapeuten lieben ihren Beruf. Dennoch ist die Arbeit mit kranken Menschen immer schwer und unberechenbar. Viele Erfahrungen und Erkenntnisse musste sich Rainer Holtkamp im Laufe seiner Berufstätigkeit von fast 30 Jahren selbst erarbeiten. In seiner Tätigkeit als Dozent und Supervisor konnte er viele Fragen der Kandidaten sammeln und daraus Interventionen erarbeiten.</p>
      <p>Interventionen, die meist in keinem Lehrbuch stehen. Mit vielen dieser Interventionen wird die psychotherapeutische Arbeit leichter und macht auch mehr Freude. Und wer mit Freude als Psychotherapeut in die Praxis geht, 'arbeitet' im Sinne von Konfuzius auch nicht mehr. Neben unkonventionellen und überraschenden Interventionen macht sich Rainer Holtkamp essayistisch auch über Wirkfaktoren der Psychotherapie und Schwierigkeiten bzw. Grenzen der Behandlung Gedanken. Deshalb ist das Buch auch etwas dicker geworden. Da es ein Lesebuch sein soll, muss niemand alles lesen.</p>
    </div>
    <p class="back-audience">nur Psychotherapeuten</p>
  </section>
</body>
</html>
```